We need a flyer for Lotus Tide Gathering

Please see the brief.doc attachment for full details

We need 2 formats/sizes:
1 - Standard A5 size
2- Facebook Cover Size

Thanks

```html
<!DOCTYPE html>
<html lang="en">
<head>
<meta charset="utf-8">
<title>Lotus Tide Gathering Flyer</title>
<link href="https://fonts.googleapis.com/css2?family=Arimo:wght@400;700&display=swap" rel="stylesheet">
<style>
  :root {
    --sun-core: #fde9a6;
    --sun-mid: #f9b858;
    --sun-edge: #ee8420;
    --gold: #d9a441;
    --band: #ffffff;
    --ink: #3a2a1a;
    --brand: #c9782a;
    --pool: #4fb7d8;
    --deck: #d9d2c2;
    --footer-bg: rgba(255,255,255,0.55);
  }
  * { margin: 0; padding: 0; box-sizing: border-box; }
  html, body { width: 867px; height: 1200px; overflow: hidden; background: #ffffff; }
  body { font-family: "Arimo", Arial, sans-serif; color: var(--ink); }
  .flyer {
    position: relative; width: 867px; height: 1200px; overflow: hidden;
    background: radial-gradient(circle at 50% 64%, var(--sun-core) 0%, var(--sun-mid) 38%, var(--sun-edge) 100%);
  }
  .hero-photo {
    position: absolute; left: 0; top: 0; width: 867px; height: 540px;
    background: linear-gradient(180deg, #cfe6d8 0%, #8fbf9a 22%, var(--pool) 45%, #3aa2c6 62%, var(--deck) 80%, #c9bfac 100%);
  }
  .swoosh { position: absolute; left: 0; top: 440px; width: 867px; height: 260px; }
  .brand {
    position: absolute; left: 48px; top: 540px; height: 40px;
    display: flex; align-items: center; gap: 14px;
  }
  .brand-dot { width: 26px; height: 26px; border-radius: 50%; background: var(--gold); }
  .brand-name { font-size: 34px; line-height: 40px; font-weight: 700; color: var(--brand); }
  .intro {
    position: absolute; left: 70px; top: 725px; width: 727px;
    font-size: 20px; line-height: 1.55; text-align: center; color: var(--ink);
  }
  .contact-bar {
    position: absolute; left: 30px; top: 1085px; width: 807px; height: 46px;
    background: var(--footer-bg); border-radius: 4px;
    display: flex; align-items: center; justify-content: space-around;
    font-size: 16px;
  }
  .contact-item { display: flex; align-items: center; gap: 7px; }
  .contact-item svg { width: 20px; height: 20px; }
  .social-dot { width: 18px; height: 18px; border-radius: 50%; background: var(--brand); }
  .website { position: absolute; left: 0; top: 1146px; width: 867px; text-align: center; font-size: 16px; }
</style>
</head>
<body>
<main class="flyer">
  <div class="hero-photo" role="img" aria-label="Photo of a woman holding a yoga backbend pose beside a pool with palms and a lawn behind"></div>

  <svg class="swoosh" viewBox="0 0 867 260" preserveAspectRatio="none" aria-hidden="true">
    <path d="M0 80 C 280 40, 580 20, 867 30 L867 140 C 600 130, 300 170, 0 250 Z" fill="var(--band)"/>
    <path d="M0 250 C 300 170, 600 130, 867 140" fill="none" stroke="var(--gold)" stroke-width="6"/>
    <path d="M0 80 C 280 40, 580 20, 867 30" fill="none" stroke="var(--gold)" stroke-width="3"/>
  </svg>

  <div class="brand">
    <span class="brand-dot"></span>
    <span class="brand-name">Lotus Tide Gathering</span>
  </div>

  <p class="intro">Lorem Ipsum is simply dummy text of the printing and typesetting industry. Lorem Ipsum has been the industry's standard dummy text ever since the 1500s, when an unknown printer took a galley of type and scrambled it to make a type specimen book. It has survived not only five centuries, but also the leap into electronic typesetting, remaining essentially unchanged. It was popularised in the 1960s with the release of Letraset sheets containing Lorem Ipsum passages, and more recently with desktop publishing software like Aldus PageMaker including versions of Lorem Ipsum.</p>

  <div class="contact-bar">
    <span class="contact-item">
      <svg viewBox="0 0 20 20" aria-hidden="true"><rect x="1" y="4" width="18" height="12" rx="2" fill="var(--brand)"/><path d="M2 5 L10 11 L18 5" fill="none" stroke="#fff" stroke-width="1.5"/></svg>
      info@lotustide.example
    </span>
    <span class="contact-item">
      <svg viewBox="0 0 20 20" aria-hidden="true"><path d="M5 2 L8 2 L9 6 L7 8 C8 11 9 12 12 13 L14 11 L18 12 L18 15 C18 17 16 18 14 18 C7 17 3 13 2 6 C2 4 3 2 5 2 Z" fill="var(--brand)"/></svg>
      74120583
    </span>
    <span class="contact-item"><span class="social-dot"></span>lotustide</span>
    <span class="contact-item"><span class="social-dot"></span>lotustide</span>
    <span class="contact-item"><span class="social-dot"></span>lotustide</span>
  </div>
  <p class="website">www.lotustide.example</p>
</main>
</body>
</html>
```